Need DL Flyer for Real Estate Drops

We need a real estate flyer ,double sided. With content on 1 side like: Want to know what's your house is worth " contact us today and on other side agent details. We are looking for an ongoing partnership with designer so this assignment will be ongoing

```html
<!DOCTYPE html>
<html lang="en">
<head>
<meta charset="utf-8">
<title>Meridian Real Estate – DL Flyer</title>
<link rel="stylesheet" href="https://fonts.googleapis.com/css2?family=Open+Sans:wght@300;400;600;700&display=swap">
<style>
  :root {
    --navy: #141b3b;
    --red: #d42a32;
    --white: #ffffff;
    --page: #e6e6e6;
    --sky: #a9c6e4;
    --house: #7c8794;
    --lawn: #4f7a3a;
    --suit: #1f2c4a;
    --skin: #b98a72;
  }
  * { box-sizing: border-box; margin: 0; padding: 0; }
  html, body { width: 1161px; height: 1200px; overflow: hidden; }
  body {
    background: var(--page);
    font-family: "Open Sans", Arial, sans-serif;
    color: var(--white);
    position: relative;
  }
  .flyer {
    position: absolute;
    left: 69px;
    width: 1022px;
    height: 488px;
    background: var(--navy);
    overflow: hidden;
  }
  .flyer--front { top: 77px; }
  .flyer--back { top: 645px; }

  .photo { position: absolute; inset: 0; }
  .stripe { position: absolute; inset: 0; background: var(--white); }

  .flyer--front .stripe { clip-path: polygon(392px 0, 1022px 0, 1022px 488px, 599px 488px); }
  .flyer--front .photo {
    clip-path: polygon(404px 0, 1022px 0, 1022px 488px, 611px 488px);
    background: linear-gradient(180deg, var(--sky) 0%, #c9d6e2 22%, var(--house) 45%, #6b7480 65%, var(--lawn) 82%, #3f5f30 100%);
  }
  .flyer--back .stripe { clip-path: polygon(0 0, 640px 0, 511px 488px, 0 488px); }
  .flyer--back .photo {
    clip-path: polygon(0 0, 627px 0, 498px 488px, 0 488px);
    background: linear-gradient(135deg, #2a3a5c 0%, var(--suit) 35%, var(--skin) 60%, #a4443b 72%, var(--suit) 100%);
  }

  .brand {
    position: absolute;
    display: flex;
    align-items: center;
    gap: 14px;
    white-space: nowrap;
  }
  .brand__mark {
    width: 50px;
    height: 50px;
    flex: none;
    background: var(--red);
  }
  .brand__name {
    font-weight: 600;
    font-size: 29px;
    line-height: 1;
    color: var(--white);
    letter-spacing: -0.3px;
  }
  .flyer--front .brand { left: 26px; top: 48px; }
  .flyer--back .brand { left: 600px; top: 78px; }

  .headline {
    position: absolute;
    left: 40px;
    top: 226px;
    width: 400px;
    text-align: center;
    font-weight: 400;
    font-size: 32px;
    line-height: 1.3;
  }
  .call-button {
    position: absolute;
    left: 86px;
    top: 338px;
    width: 326px;
    height: 44px;
    border-radius: 22px;
    background: var(--red);
    display: flex;
    align-items: center;
    justify-content: center;
    gap: 10px;
    font-weight: 700;
    font-size: 18px;
  }
  .call-button svg { width: 18px; height: 18px; }
  .appraisal-note {
    position: absolute;
    left: 22px;
    top: 399px;
    width: 520px;
    font-size: 12.5px;
    font-weight: 600;
    text-transform: uppercase;
    letter-spacing: -0.1px;
  }
  .appraisal-note strong { font-weight: 700; }

  .address-band {
    position: absolute;
    background: var(--red);
    display: flex;
    align-items: center;
    font-weight: 700;
    font-size: 14px;
  }
  .flyer--front .address-band {
    left: 0; top: 437px; width: 568px; height: 51px;
    clip-path: polygon(0 0, 546px 0, 568px 51px, 0 51px);
    padding-left: 30px;
    gap: 8px;
  }
  .flyer--back .address-band {
    left: 512px; top: 428px; width: 510px; height: 60px;
    clip-path: polygon(16px 0, 510px 0, 510px 60px, 0 60px);
    justify-content: center;
    padding-left: 20px;
  }

  .agent {
    position: absolute;
    left: 600px;
    top: 232px;
  }
  .agent__title {
    font-weight: 300;
    font-size: 22px;
    margin-bottom: 16px;
  }
  .contact-list { list-style: none; }
  .contact-list li {
    display: flex;
    align-items: center;
    gap: 14px;
    font-weight: 300;
    font-size: 19px;
    height: 38.5px;
  }
  .contact-list svg { width: 20px; height: 20px; flex: none; }
</style>
</head>
<body>

  <section class="flyer flyer--front" aria-label="Flyer front">
    <div class="stripe"></div>
    <div class="photo" role="img" aria-label="Photo of a two-storey suburban house with the agent standing in front in a light grey suit"></div>

    <div class="brand">
      <span class="brand__mark"></span>
      <span class="brand__name">Meridian Real Estate</span>
    </div>

    <h1 class="headline">Want to know what's your house is worth?</h1>

    <div class="call-button">
      <span>CALL ME NOW!</span>
      <svg viewBox="0 0 24 24" aria-hidden="true"><circle cx="12" cy="12" r="10.5" fill="none" stroke="#fff" stroke-width="2"/><path d="M8.6 6.8l1.8 2.4-1 1.3c.7 1.5 1.9 2.8 3.5 3.6l1.3-1 2.4 1.8-.8 1.9c-4.4-.4-8.4-4.4-8.9-8.9z" fill="#fff"/></svg>
      <span>03 9400 1234</span>
    </div>

    <p class="appraisal-note">Call <strong>Rohan Kessler</strong> to arrange your free property appraisal!</p>

    <div class="address-band">
      <span>14/8 Harbour Ln, Westfield, VIC 3100</span>
      <span>|</span>
      <span>www.meridianrealty.com.au</span>
    </div>
  </section>

  <section class="flyer flyer--back" aria-label="Flyer back">
    <div class="stripe"></div>
    <div class="photo" role="img" aria-label="Photo of two hands sheltering a small red model house"></div>

    <div class="brand">
      <span class="brand__mark"></span>
      <span class="brand__name">Meridian Real Estate</span>
    </div>

    <div class="agent">
      <p class="agent__title">Rohan Kessler, Managing Director</p>
      <ul class="contact-list">
        <li>
          <svg viewBox="0 0 24 24" aria-hidden="true"><circle cx="12" cy="12" r="10.5" fill="none" stroke="#fff" stroke-width="1.8"/><path d="M8.6 6.8l1.8 2.4-1 1.3c.7 1.5 1.9 2.8 3.5 3.6l1.3-1 2.4 1.8-.8 1.9c-4.4-.4-8.4-4.4-8.9-8.9z" fill="#fff"/></svg>
          03 9400 1234
        </li>
        <li>
          <svg viewBox="0 0 24 24" aria-hidden="true"><circle cx="12" cy="12" r="11" fill="#fff"/><rect x="6.5" y="8" width="11" height="8" rx="1" fill="var(--navy)"/><path d="M6.8 8.5l5.2 4 5.2-4" fill="none" stroke="#fff" stroke-width="1.2"/></svg>
          rohan@meridianrealty.com.au
        </li>
        <li>
          <svg viewBox="0 0 24 24" aria-hidden="true"><circle cx="12" cy="12" r="10.5" fill="none" stroke="#fff" stroke-width="1.8"/><circle cx="12" cy="12" r="6" fill="none" stroke="#fff" stroke-width="1.3"/><ellipse cx="12" cy="12" rx="2.6" ry="6" fill="none" stroke="#fff" stroke-width="1.2"/><path d="M6 12h12" stroke="#fff" stroke-width="1.2"/></svg>
          www.meridianrealty.com.au
        </li>
      </ul>
    </div>

    <div class="address-band">14/8 Harbour Ln, Westfield, VIC 3100</div>
  </section>

</body>
</html>
```